Dental Practice Billboard Design

We are a newer dental practice in need of a simple but appealing billboard for our growing dental practice to attract new patients. The practice is owned by husband and wife dentists and is family friendly in a small town in Kentucky. We try to be very friendly and caring to our patients. Would prefer a blue background for the billboard and our tooth logo to be prominent. We are partial to the Patua One font used in the image below but please feel free to tweak it as you deem necessary. The shape of the uppercase D and lowercase g are why we like that font, so fonts with a similarly shaped “D” and “g” would work as well. Please include our phone number (606) 847-3962. Please see our website Harlowfamilydentistry.com for more info on the practice if needed. Thank you! Looking forward to seeing your creation.
Updates

The dimensions will be 12ft x 24ft (3.6576m x 7.3152m). Apologies for not including this in the original prompt. Thank you all for your submissions.

Industry/Entity Type

Dental

Font styles to use
Other font styles liked:
• Patua One

Colors
0054AA
0677BA
7BADD7
CADEEF
E8F1F8
0094D4
00A9DD
6FCCEA
C7EBF8
E9F6FB
00AB8E
00BBA5
67D7C9
C6EFE9
E9F9F6
59FF00
82FF00
B8FF75
E3FFCB
F4FFEA

Requirements
Must have
• Phone number, website, Logo, Practice name “Harlow Family Dentistry”
Should not have
• A tagline or slogan

```html
<!DOCTYPE html>
<html lang="en">
<head>
<meta charset="utf-8">
<title>Harlow Family Dentistry Billboard</title>
<link href="https://fonts.googleapis.com/css2?family=Patua+One&display=swap" rel="stylesheet">
<style>
  :root {
    --navy-deep: #03021a;
    --navy: #0e0b30;
    --navy-light: #1a1447;
    --green: #14ae17;
    --blue: #0257bd;
    --white: #ffffff;
    --mark-tint: #e8f1f8;
  }
  html, body {
    margin: 0;
    padding: 0;
    width: 1200px;
    height: 600px;
    overflow: hidden;
    background: var(--white);
  }
  .billboard {
    display: block;
    width: 1200px;
    height: 600px;
  }
  .website { font-family: "Patua One", serif; fill: var(--white); }
  .website-rule { fill: var(--green); }
  .phone-number { font-family: "Patua One", serif; fill: var(--white); }
  .practice-name { font-family: "Patua One", serif; fill: var(--blue); }
  .name-mark { fill: var(--mark-tint); }
</style>
</head>
<body>
<svg class="billboard" viewBox="0 0 1200 600" xmlns="http://www.w3.org/2000/svg">
  <defs>
    <radialGradient id="navyGlow" cx="0.25" cy="0.85" r="0.9">
      <stop offset="0" stop-color="var(--navy-light)"/>
      <stop offset="0.6" stop-color="var(--navy)"/>
      <stop offset="1" stop-color="var(--navy-deep)"/>
    </radialGradient>
  </defs>

  <rect class="backdrop" width="1200" height="600" fill="url(#navyGlow)"/>

  <path class="panel-edge" fill="var(--blue)"
        d="M913,0 C790,75 748,230 716,350 C696,430 686,455 676,470 L676,600 L1200,600 L1200,0 Z"/>
  <path class="panel-white" fill="var(--white)"
        d="M913,0 C808,75 768,230 738,350 C720,430 708,455 694,470 L694,600 L1200,600 L1200,0 Z"/>

  <polygon class="band-stripe" fill="var(--blue)" points="0,470 808,470 745,600 0,600"/>
  <polygon class="band-green" fill="var(--green)" points="0,470 787,470 724,600 0,600"/>

  <!-- website -->
  <text class="website" x="74" y="262" font-size="54" textLength="600" lengthAdjust="spacingAndGlyphs">Harlowfamilydentistry.com</text>
  <rect class="website-rule" x="74" y="290" width="600" height="6"/>

  <!-- phone -->
  <text class="phone-number" x="74" y="560" font-size="92" textLength="576" lengthAdjust="spacingAndGlyphs">(606) 847-3962</text>

  <!-- practice name -->
  <circle class="name-mark" cx="1003" cy="262" r="125"/>
  <text class="practice-name" x="864" y="527" font-size="86" textLength="287" lengthAdjust="spacingAndGlyphs">Harlow</text>
  <text class="practice-name" x="864" y="571" font-size="38" textLength="285" lengthAdjust="spacingAndGlyphs">Family Dentistry</text>
</svg>
</body>
</html>
```